Business Card Design Project

We are a commercial talent casting company, a very "now" company. We need a new business card that is both current, graphic and elegantly interesting. As we are a service business,
we need something that will attract the attention of new clients,
yet project a business that is 25 years old.

Industry/Entity Type

Business

Requirements
Must have
• 1. Logo - Nora Quillan Casting
2. Address - 47 Harwick Street
New York, New York 10027
3. Phone - 212-638-4170
4. E-Mail - Casting@noraquillan.com

Nice to have
• Would like the card in black and white with the only accent
color being red.

```html
<!DOCTYPE html>
<html lang="en">
<head>
<meta charset="UTF-8">
<title>Nora Quillan Casting – Business Card</title>
<link rel="stylesheet" href="https://fonts.googleapis.com/css2?family=Aldrich&display=swap">
<style>
  :root {
    --page-bg: #ffffff;
    --band-top: #0d0d0d;
    --band-bottom: #3a3a3a;
    --panel-top: #e9e9e9;
    --panel-bottom: #ffffff;
    --accent-red: #d4141b;
    --accent-red-dark: #9e0c10;
    --ink: #111111;
  }

  html, body {
    margin: 0;
    padding: 0;
    width: 1200px;
    height: 849px;
    overflow: hidden;
    background: var(--page-bg);
  }

  .canvas {
    position: relative;
    width: 1200px;
    height: 849px;
  }

  .business-card {
    position: absolute;
    left: 120px;
    top: 150px;
    width: 960px;
    height: 549px;
    background: linear-gradient(to bottom, var(--panel-top), var(--panel-bottom) 45%);
    box-shadow: 0 6px 22px rgba(0, 0, 0, 0.28);
    overflow: hidden;
    font-family: "Aldrich", sans-serif;
  }

  .header-band {
    position: absolute;
    left: 0;
    top: 0;
    width: 100%;
    height: 285px;
    background: linear-gradient(to bottom, var(--band-top), var(--band-bottom));
  }

  .company-name {
    position: absolute;
    left: 0;
    right: 0;
    top: 112px;
    margin: 0;
    text-align: center;
    font-size: 48px;
    font-weight: 400;
    letter-spacing: 0.5px;
    color: var(--accent-red);
    text-shadow: 0 2px 3px rgba(0, 0, 0, 0.6);
  }

  .edge-bar {
    position: absolute;
    width: 9px;
    height: 210px;
    background: linear-gradient(to right, var(--accent-red), var(--accent-red-dark));
    border-radius: 5px;
  }

  .edge-bar--left {
    left: -4px;
    top: 170px;
  }

  .edge-bar--right {
    right: -4px;
    top: 120px;
  }

  .contact-block {
    position: absolute;
    margin: 0;
    font-size: 22px;
    line-height: 1.3;
    color: var(--ink);
    font-style: normal;
  }

  .contact-block .label {
    color: var(--accent-red);
  }

  .address {
    left: 72px;
    top: 400px;
  }

  .reach {
    left: 600px;
    top: 322px;
    font-size: 19px;
  }
</style>
</head>
<body>
  <main class="canvas">
    <section class="business-card" aria-label="Nora Quillan Casting business card">
      <div class="header-band">
        <h1 class="company-name">Nora Quillan Casting</h1>
      </div>

      <span class="edge-bar edge-bar--left" aria-hidden="true"></span>
      <span class="edge-bar edge-bar--right" aria-hidden="true"></span>

      <address class="contact-block address">
        <span class="label">Adress:</span> 47 Harwick Street<br>
        New York, New York 10027
      </address>

      <address class="contact-block reach">
        <span class="label">Phone:</span> 212-638-4170<br>
        <span class="label">Email:</span> Casting@noraquillan.com
      </address>
    </section>
  </main>
</body>
</html>
```